Global Outreach Fellowship needs a Book Cover Design Project

I am a pastor, missionary, author, and the founder of a non-profit organization. I am in the process of publishing a book focused on "The Spirit of a Faithful Shepherd" and desire a contemporary, even somewhat abstract book cover. Here is a link to the company's web page portfolio that designed our Web Page, to give you an idea of the style of cover that I am looking for. http://www.pixelharborstudio.com/cd-covers

Though the book is obviously targeted toward Christians, I want it to be attractive enough to capture the attention of the general population as well.

Industry/Entity Type

Non-Profit

```html
<!DOCTYPE html>
<html lang="en">
<head>
<meta charset="utf-8">
<title>The Spirit of a Faithful Shepherd — Cover Spread</title>
<link href="https://fonts.googleapis.com/css2?family=Cinzel:wght@400;700&display=swap" rel="stylesheet">
<style>
  :root {
    --paper: #ffffff;
    --accent-purple: #7a2a86;
    --accent-blue: #1ea6e6;
    --frame-grey: #c9ccd4;
    --mark-grey: #b5b8bf;
    --skin-light: #f3d9cc;
    --skin-mid: #e7b9a6;
    --heart-pink: #d9709a;
    --haze: #eef1f6;
  }
  * { margin: 0; padding: 0; box-sizing: border-box; }
  html, body { width: 1200px; height: 900px; overflow: hidden; background: var(--paper); }
  .spread { position: relative; width: 1200px; height: 900px; background: var(--paper); font-family: "Cinzel", serif; }

  .back-panel-frame {
    position: absolute; left: 240px; top: 186px; width: 294px; height: 526px;
    border: 1px solid var(--frame-grey); background: var(--paper);
  }

  .spine-marks { position: absolute; left: 0; top: 0; width: 1200px; height: 900px; }

  .cover-photo {
    position: absolute; left: 440px; top: 300px; width: 580px; height: 460px;
    background:
      radial-gradient(ellipse 14% 12% at 67% 53%, var(--heart-pink) 0%, rgba(217,112,154,0.6) 55%, rgba(217,112,154,0) 100%),
      radial-gradient(ellipse 42% 30% at 62% 58%, var(--skin-mid) 0%, var(--skin-light) 55%, rgba(243,217,204,0) 100%),
      radial-gradient(ellipse 55% 42% at 55% 52%, var(--haze) 0%, rgba(238,241,246,0.7) 60%, rgba(255,255,255,0) 100%);
  }

  .spine-title {
    position: absolute; left: 588px; top: 158px;
    writing-mode: vertical-rl;
    display: flex; align-items: center; gap: 10px;
    font-size: 16px; letter-spacing: 0.5px; color: var(--accent-blue);
    white-space: nowrap;
  }
  .spine-title .spine-square { width: 9px; height: 9px; background: var(--accent-purple); display: block; }

  .front-title {
    position: absolute; left: 640px; top: 244px; width: 300px;
    text-align: center; line-height: 1;
  }
  .front-title .title-lead {
    display: block; font-weight: 700; font-size: 17px; color: var(--accent-purple); letter-spacing: 0.5px;
  }
  .front-title .title-main {
    display: block; font-weight: 400; font-size: 42px; color: var(--accent-blue); margin-top: 6px; letter-spacing: 1px;
  }
  .front-title .title-main + .title-main { margin-top: 2px; }
</style>
</head>
<body>
  <div class="spread">
    <div class="back-panel-frame"></div>

    <div class="cover-photo" role="img" aria-label="Soft photograph of open cupped hands holding a small pink paper heart, fading into white"></div>

    <svg class="spine-marks" width="1200" height="900" aria-hidden="true">
      <g stroke="var(--mark-grey)" stroke-width="1.5">
        <line x1="580" y1="104" x2="580" y2="132"/>
        <line x1="618" y1="104" x2="618" y2="132"/>
        <line x1="580" y1="770" x2="580" y2="798"/>
        <line x1="618" y1="770" x2="618" y2="798"/>
      </g>
    </svg>

    <div class="spine-title">
      <span class="spine-square"></span>
      <span>THE SPIRIT OF A FAITHFUL SHEPHERD</span>
    </div>

    <h1 class="front-title">
      <span class="title-lead">THE SPIRIT OF A</span>
      <span class="title-main">FAITHFUL</span>
      <span class="title-main">SHEPHERD</span>
    </h1>
  </div>
</body>
</html>
```